College Apartment Leasing Flyer

We need a post card/flyer design for a college apartment rental company called RV Stewardship Partners. We lease apartments to college students and would like a post card/flyer that appeal to college students, that are bright colors and eye catching. We would like pictures showcasing our properties with various amenities including big kitchens, living rooms with 50 inch flat screen TVs, large outdoor patios, large rooftop decks, private bathrooms, and much more. Granite countertops, hardwood floors, ceiling fans are some of the many amenities these apartments offer college students.

We want a flyer that advertises these apartments based on the pictures attached, and advertising that we are beginning to kick off our new leasing season. These apartments are ready to be rented, and we are looking to advertise these apartments to Harrowfield College college students looking for apartments.
Updates

Project Deadline Extended
Reason: I would like to see fun design elements incorporated into the flyer. Big, bold print and pictures are the main attraction

Target Market(s)

College students

Industry/Entity Type

Real Estate

Font styles to use
Sans Serif

Colors
abd037
6b449b

Requirements
Must have
• Bright colors, big bold print, pictures of college apartments
Nice to have
• I would like to see multiple pictures with BIG print
Should not have
• Animated pictures

```html
<!DOCTYPE html>
<html lang="en">
<head>
<meta charset="utf-8">
<title>RV Stewardship Partners – Leasing Flyer</title>
<link rel="stylesheet" href="https://fonts.googleapis.com/css2?family=Open+Sans:wght@300;400;600;700&display=swap">
<style>
  :root {
    --purple: #6b449b;
    --green: #abd037;
    --ink: #3a3a3a;
    --grey: #555555;
    --paper: #ffffff;
    --sky-top: #1d4f94;
    --sky-bottom: #9cc3e6;
    --room-warm: #b5714a;
    --room-light: #e9e2d8;
  }
  * { margin: 0; padding: 0; box-sizing: border-box; }
  html, body { width: 900px; height: 1200px; overflow: hidden; background: var(--paper); }
  body { font-family: "Open Sans", Arial, sans-serif; color: var(--ink); }

  .flyer { position: relative; width: 900px; height: 1200px; background: var(--paper); }

  .hero-photo {
    position: absolute; left: 0; top: 0; width: 900px; height: 470px;
    background: linear-gradient(180deg, var(--sky-top) 0%, #3f78b8 45%, var(--sky-bottom) 72%, #c9c6c0 73%, #a9a6a0 100%);
  }

  .inset-photo {
    position: absolute; left: 40px; top: 440px; width: 300px; height: 260px;
    border: 8px solid var(--paper);
    background: linear-gradient(135deg, var(--room-light) 0%, #d8cfc3 40%, var(--room-warm) 70%, #6e3d25 100%);
    box-shadow: 0 2px 8px rgba(0,0,0,0.2);
  }

  .description { position: absolute; left: 370px; top: 485px; width: 490px; }
  .description h2 {
    font-weight: 400; font-size: 34px; letter-spacing: 1px; color: var(--purple); margin-bottom: 8px;
  }
  .description p { font-size: 14.5px; line-height: 1.45; color: var(--grey); }

  .amenities {
    position: absolute; left: 40px; top: 720px; width: 820px; height: 190px;
    background: var(--purple); color: var(--paper); padding: 12px 70px 0;
  }
  .amenities h2 {
    text-align: center; font-weight: 400; font-size: 27px; letter-spacing: 1px; margin-bottom: 8px;
  }
  .amenity-columns { display: flex; gap: 120px; }
  .amenity-columns ul { list-style: none; width: 260px; }
  .amenity-columns li { font-size: 13.5px; line-height: 1.42; padding-left: 14px; position: relative; }
  .amenity-columns li::before { content: "•"; position: absolute; left: 0; }

  .brand { position: absolute; left: 40px; top: 950px; width: 360px; }
  .brand-mark { display: flex; align-items: center; gap: 14px; }
  .brand-square { width: 34px; height: 34px; background: var(--purple); flex: none; }
  .brand-name { font-size: 30px; font-weight: 300; color: var(--grey); line-height: 1.15; }

  .info-box {
    position: absolute; left: 450px; top: 945px; width: 450px; height: 180px;
    background: var(--green); display: flex; align-items: flex-start; padding: 24px 30px;
    color: var(--paper);
  }
  .info-box h3 { font-size: 22px; font-weight: 600; letter-spacing: 0.5px; margin-bottom: 14px; }
  .info-box p { font-size: 17px; line-height: 1.45; }
  .address { width: 220px; }
  .divider { width: 2px; height: 130px; background: var(--paper); margin: 0 26px; }
  .square-feet p { font-size: 17px; }
</style>
</head>
<body>
<main class="flyer">
  <div class="hero-photo" role="img" aria-label="Photo of a large rooftop deck under a blue sky with the city skyline behind"></div>

  <div class="inset-photo" role="img" aria-label="Photo of an apartment interior with a spiral staircase and a granite kitchen"></div>

  <section class="description">
    <h2>DESCRIPTION</h2>
    <p>NEW Construction blocks from Harrowfield College! Beautiful 4BR/3.5BA unit on Alder St. with upgraded amenities including: GRANITE COUNTER TOPS, NEW APPLIANCES, SPACIOUS BEDROOMS AND CLOSETS, HARDWOOD FLOORS, SECURITY SYSTEM, OUTDOOR PATIO, SECURITY CAMERAS, SURROUND SOUND IN LIVING ROOM AND PATIO, CEILING FANS, WASHER AND DRYER, AND MORE!</p>
  </section>

  <section class="amenities">
    <h2>AMENITIES</h2>
    <div class="amenity-columns">
      <ul>
        <li>4 Bedrooms</li>
        <li>3.5 Bathrooms</li>
        <li>Touch Screen Security System</li>
        <li>Outdoor Patio</li>
        <li>Security Cameras</li>
        <li>Surround sound in Living Room and Outdoor Patio</li>
      </ul>
      <ul>
        <li>Spacious Bedrooms &amp; Closets</li>
        <li>High Ceilings</li>
        <li>Granite Counter Tops</li>
        <li>Hardwood Floors</li>
        <li>In Unit Washer/Dryer</li>
        <li>Central Air/Heat</li>
        <li>New Appliances</li>
      </ul>
    </div>
  </section>

  <section class="brand">
    <div class="brand-mark">
      <span class="brand-square"></span>
      <span class="brand-name">RV Stewardship Partners</span>
    </div>
  </section>

  <section class="info-box">
    <div class="address">
      <h3>PROPERTY ADDRESS</h3>
      <p>1728 Alder Street<br>Philadelphia, PA 19121</p>
    </div>
    <div class="divider"></div>
    <div class="square-feet">
      <h3>SQUARE FEET:</h3>
      <p>AVAILABLE:<br>8/4/15</p>
    </div>
  </section>
</main>
</body>
</html>
```